Tradeshow Booth, Banners & Brochure Design

Corvi Lattice (www.corvilattice-example.com) is a Nortwell Affiliate specializing in developing products and customizations for Nortwell Ledgerline KX. The purpose of this project is to develop a unified approach to graphic design for our tradeshow booth, banners and product literature. This should result in completed designs for the booth and banners, and several templates that can be used to create our product literature.

***WE WILL ONLY LOOK THROUGH THE FIRST 100 SUBMISSIONS***

Reason: We have received some requests for an extended deadline, and we would like to encourage more submissions, so we are extending the deadline by two days. Please let us know if you have any questions or need clarification on our design brief.

Thanks for the submissions and questions everyone.  I will get answers to your questions, and more detailed specs, posted within the next couple of hours.  I will also provide detailed feedback to your designs within that time.

Q:  How large should each item be – what is the approximate number of words/lines, columns/rows?

 

-          We have updated the Content Type list to cut it down and simplify this.  For word count, we are attaching the text for our NEW brochure on WMS, which we intend to be a 4 page brochure.  We have labeled each section according to content type.  This can be used as a guide for how much text each content area must be able to accommodate.  You can even pull the raw text straight from the word file for your design.  The RVOT brochure, already included, is an OLD brochure, and represents a design that we are trying to evolve beyond.

 

-          Keep in mind that the 4 page product brochure will be a 17” by 11” single sheet, folded.  The 2 page product brochure will be a single 8.5” by 11” sheet, printed on both sides.

 

-          For the 2 page product brochure, assume something that looks like half of the 4 page design.  For example, we will be creating one brochure for “Financials” which comprises two products.  Product A will go on the front, and Product B on the back.  We will still need to allow for contact information and the other content types as specified.

 

-          For the 4 page corporate overview, we have attached our current corporate overview for reference, and labeled the content types.  Again, feel free to pull raw text directly from this for purposes of your design – though remember, this OLD brochure represents a design we are trying to evolve beyond.

 

-          For images (screenshots, stock photography, diagrams, etc) we are thinking we would like to see about 4 on the 4 page brochure, but only 1-2 for the 2 page brochure.  The corporate overview can have suitable imagery at your discretion.

 

-          We would like to see some of the imagery used in the Tradeshow materials (booth, banners) carried across to the brochures.

 

 

 

Q:  What are the detailed print guidelines, especially in relation to bleeds, etc?

 

-          For all the brochures, use a full bleed.  If your design incorporates a bleed of color across a fold, try to have the bleed going across no more than 25% of the height of the page.  CMYK color, 300DPI, 8.5”w x 11”h.  We will most likely go with 100# paper without too much gloss on it. 

 

-          For all other materials such as booth and banners, no bleeds.  Please see specification sheets for the booth and banners, included below.  Create your designs to the exact size given.

 

 

 

Q:  Will booth graphics be printed as one continuous piece, or will they be applied in sections that are in line with the panel dimensions of the 8 center panels and end caps?

 

-          Graphics are printed as one continuous piece on a large format printer.  They are then cut into the individual panel pieces for shipping and storage.  When the booth is fully assembled, the seams are hardly noticeable unless you are looking for them from a short distance away.

 

-          We are already in possession of one 10’ booth, and will be ordering another, with the associated pieces, to create the 20’ booth.  The booth comprises a support structure, and the actual graphics panels which are attached to the front.  The overall 20’ design should take into account the fact that we will, in the future, attend tradeshows with only a 10’ booth, so only half of the panels will be used.  We would like to be able to mix and match our four categories to suit the show.

Reason: We are extending the deadline one more time to allow Tamsin and anyone else who needs the extra time for the brochure design.

Please prioritize your brochure design at this time.  We are interested in receiving feedback on deadlines - if you can confirm that you will submit a design but need more time to do so, we would like to hear from you.

Reason: To provide time for solid designs from all the designers who have been invited, we are extended the deadline one more time. This will be the final extension.

Target Market(s)

Corporate Clients

Industry/Entity Type

Graphic Design

Requirements
Must have
• TRADESHOW SPECIFIC
1. Graphics for 10'x20' “Gullwing” Tradeshow Booth
a. Layout should approximate the grid we have mocked up in our preliminary layout – see below. There is a fair amount of flexibility so long as the basic grid, contents and dimensions are adhered to.

2. Graphics needed for 3 retractable banner stands
a. Two banner stands will have dimensions of 24” x 88”
b. The third banner stand will have dimensions of 36” x 88” and will be double-sided. The design for this banner should have the option to be scaled down to 33.5” wide, for a possible additional banner stand being considered.
c. Banners should approximate what is shown in the preliminary layout – see below.
d. All banner stands being used are able to fully extend to 92”- however, the height of the booth itself is 88” and we would like all tradeshow specific elements to be the same height.

PRODUCT LITERATURE
1. Graphic Design and Layout needed for brochures:
a. double-sided one page for Products
b. double-sided two page for Products
c. double-sided two page for Overview

2. Pages would be full bleed letter size 8.5” x 11.

3. Samples are included below to get an idea of common grids and layouts for similar publications, as well as one of our current publications for reference.

4. Product literature must include provisions for all of the content types listed in that document, included below. There is some leeway with image placement – a product brochure doesn’t necessarily have to have stock photos, diagrams, AND software screenshots.

5. The designer will need to indicate what specs are required for software screenshots so that we can generate appropriate files for that use.

COMMON ELEMENTS
• Images need to include stock photos of people in business settings, as well as stock photos related to warehousing, barcoding systems, and supply chains. Other images to be used should include schematics, workflow diagrams, and other items that are related to the areas in which the company works. Each heading on the booth, and each page on the brochures, will need one image at minimum. Images and content laid out next to each other should be thematically related whenever possible. We will also create a small number of simple diagrams in house that will need to be redesigned and recreated in the appropriate format and placed in the designs.
• Clean, high-impact design. The Nortwell Quantive Bookkeeping brochure, included below, is a good example of this.
• Our current logo, included below, needs to have the tagline removed. We are also requesting that a different version of the graphic element in the logo be created, in monochrome but with roughly the same geometry.
• Our new tagline is “Integrated Solutions for Ledgerline KX” but it should not be located directly in the logo area as our current tagline is, “Making systems business-ready”.
• Designs should be produced in print-ready PDF files. We will be using Quillmark Layoutry V9 to open the PDF files, drop in our copy and other content, and finalize the designs. The PDF files will then be sent directly to our booth production and brochure printing companies.

```html
<!DOCTYPE html>
<html lang="en">
<head>
<meta charset="utf-8">
<title>Corvi Lattice – Banner and Brochure</title>
<link rel="stylesheet" href="https://fonts.googleapis.com/css2?family=Arimo:wght@400;700&family=Carlito:wght@400;700&display=swap">
<style>
  :root {
    --bg: #eceef1;
    --paper: #ffffff;
    --navy: #1c3a8a;
    --ink: #2a1a14;
    --text: #2b2b3a;
    --lavender: rgba(120, 118, 180, 0.55);
    --purple-panel: rgba(84, 86, 150, 0.82);
    --sky-top: #4f7fc4;
    --sky-mid: #c9dcf1;
    --cloud: #f4f6f9;
    --grass: #6f8c3c;
    --grass-dark: #4f6a26;
    --pattern-a: #dbeaf7;
    --pattern-b: #7fb2e0;
    --steel: #3f7fb0;
    --steel-dark: #2d6796;
    --rule: #2a2f6a;
  }
  * { box-sizing: border-box; margin: 0; padding: 0; }
  html, body { width: 1200px; height: 1200px; overflow: hidden; background: var(--bg); }
  body { position: relative; font-family: "Arimo", Arial, sans-serif; color: var(--text); }

  .piece { position: absolute; background: var(--paper); box-shadow: 0 2px 10px rgba(0,0,0,0.18); overflow: hidden; }

  /* Retractable banner */
  .banner { left: 40px; top: 105px; width: 270px; height: 990px; }
  .brand { display: flex; align-items: center; gap: 10px; }
  .brand-mark { width: 34px; height: 34px; background: var(--navy); flex: none; }
  .brand-name { font-family: "Arimo", Arial, sans-serif; font-size: 26px; color: var(--ink); font-weight: 400; }
  .banner .brand { position: absolute; left: 28px; top: 60px; }
  .banner-tagline { position: absolute; left: 0; right: 0; top: 170px; text-align: center; font-weight: 700; font-size: 27px; line-height: 1.2; color: var(--navy); }
  .banner-art { position: absolute; left: 0; right: 0; top: 400px; bottom: 0; background: linear-gradient(180deg, rgba(255,255,255,0) 0%, var(--pattern-a) 30%, var(--pattern-b) 70%, var(--pattern-a) 100%); }
  .banner-list { position: absolute; left: 42px; right: 0; top: 300px; height: 170px; background: var(--lavender); padding: 28px 0 0 30px; list-style: none; z-index: 1; }
  .banner-list li { font-size: 19px; color: #1f1f2a; line-height: 1.35; }
  .banner-list li::before { content: "• "; }

  /* Brochure cover */
  .cover { left: 340px; top: 340px; width: 400px; height: 518px; }
  .cover-photo { position: absolute; inset: 0; background: linear-gradient(180deg, var(--sky-top) 0%, var(--sky-mid) 18%, var(--cloud) 45%, #d8e4ef 70%, var(--grass) 80%, var(--grass-dark) 100%); }
  .cover .brand { position: absolute; left: 40px; top: 150px; }
  .cover .brand-mark { width: 40px; height: 40px; }
  .cover .brand-name { font-size: 27px; }
  .cover-panel { position: absolute; right: 0; top: 0; width: 150px; height: 400px; background: var(--purple-panel); border-bottom-left-radius: 46px; padding: 150px 10px 0 14px; color: #fff; font-family: "Carlito", Calibri, sans-serif; }
  .cover-title { font-size: 38px; font-weight: 700; line-height: 1.05; margin-bottom: 12px; }
  .cover-points { list-style: none; }
  .cover-points li { position: relative; padding-left: 16px; font-size: 12.5px; line-height: 1.25; margin-bottom: 6px; }
  .cover-points li::before { content: ""; position: absolute; left: 0; top: 3px; border-left: 8px solid #fff; border-top: 4.5px solid transparent; border-bottom: 4.5px solid transparent; }

  /* Inside page */
  .inside { left: 770px; top: 340px; width: 400px; height: 518px; font-family: "Carlito", Calibri, sans-serif; }
  .inside-photo { position: absolute; left: 18px; top: 18px; width: 190px; height: 130px; background: linear-gradient(180deg, var(--sky-top), var(--cloud) 75%, var(--grass)); }
  .photo-caption { position: absolute; left: 18px; top: 152px; font-size: 8px; color: #555; }
  .spine { position: absolute; left: 0; top: 170px; bottom: 0; width: 14px; background: var(--steel); }
  .spine-text { position: absolute; left: 3px; bottom: 8px; writing-mode: vertical-rl; transform: rotate(180deg); color: #fff; font-size: 8.5px; font-weight: 700; }
  .col { position: absolute; font-size: 9.5px; line-height: 1.3; color: var(--text); }
  .col p { margin-bottom: 7px; }
  .col-left { left: 24px; top: 175px; width: 176px; }
  .col-right { left: 222px; top: 130px; width: 164px; }
  .inside-points { list-style: none; }
  .inside-points li { position: relative; padding-left: 11px; margin-bottom: 3px; }
  .inside-points li::before { content: ""; position: absolute; left: 0; top: 3px; border-left: 6px solid var(--steel); border-top: 3.5px solid transparent; border-bottom: 3.5px solid transparent; }
  .callout { position: absolute; left: 250px; top: 30px; width: 130px; padding: 10px 12px; background: var(--steel); color: #fff; border-radius: 10px; font-size: 10.5px; line-height: 1.25; border: 2px solid #a9cdea; }
  .callout::after { content: ""; position: absolute; left: 60px; bottom: -12px; border-top: 12px solid var(--steel); border-right: 10px solid transparent; }
  .stats-rule { position: absolute; left: 210px; right: 0; top: 338px; height: 4px; background: var(--rule); }
  .stats { position: absolute; left: 210px; right: 0; top: 342px; bottom: 0; background: linear-gradient(180deg, var(--steel), var(--steel-dark)); padding: 10px 10px 0 12px; color: #fff; }
  .stats h2 { font-weight: 400; font-size: 15px; line-height: 1.2; margin-bottom: 8px; }
  .stat { display: flex; align-items: center; gap: 6px; margin-bottom: 7px; }
  .stat svg { flex: none; }
  .stat-value { font-size: 20px; width: 42px; flex: none; color: #0f2550; }
  .stat-note { font-size: 7.5px; line-height: 1.2; color: #fff; }
</style>
</head>
<body>

<section class="piece banner" aria-label="Retractable banner">
  <div class="brand"><span class="brand-mark"></span><span class="brand-name">Corvi Lattice</span></div>
  <h1 class="banner-tagline">Integrated<br>Solutions for<br>Ledgerline KX</h1>
  <div class="banner-art" role="img" aria-label="Soft blue pattern of rounded glass tiles fading upward"></div>
  <ul class="banner-list">
    <li>WMS &amp; Distribution</li>
    <li>Workflow</li>
    <li>Customization</li>
    <li>Financials</li>
  </ul>
</section>

<section class="piece cover" aria-label="Brochure cover">
  <div class="cover-photo" role="img" aria-label="Stock photo: a person with a cardboard box over the head leaping above a grassy field under a cloudy blue sky"></div>
  <div class="brand"><span class="brand-mark"></span><span class="brand-name">Corvi Lattice</span></div>
  <div class="cover-panel">
    <h2 class="cover-title">Lorem Ipsum?</h2>
    <ul class="cover-points">
      <li>Gia nos dolenimilit magnam il mi, tem fugia</li>
      <li>Conem et ullatus in pratum quas nescil ipsus</li>
      <li>Eum vollaut ut accaboremque magnisq uaeprorem</li>
    </ul>
  </div>
</section>

<section class="piece inside" aria-label="Brochure inside page">
  <div class="inside-photo" role="img" aria-label="Stock photo of sky and clouds over a field"></div>
  <p class="photo-caption">Ehenimus aut lab in consequat</p>
  <div class="callout">“Quas maximod es dem ut lito optatust conse”</div>

  <div class="col col-left">
    <p>Aborenimagni dit quia ne dolupti con peligen ecescit, te volectus, omnim dipsuntist, tem. Et as est, quae diatemp orest, odis iliquae seque corissit dolo voluptas dolorrovidem nis dolendest, niam fuga. Itat eatur aborerio maximolut aliqui te nus duntisseque sequi aut hitae videllu ptatiatur?</p>
    <p>Rem eaquibus earciam venim sequaestio inum demquam ut audaeru ptatam ut apidero excestrum facitatur? Pos pel id eum que quatur a perchil luptass itatat.</p>
    <ul class="inside-points">
      <li>Gia nos dolenimilit magnam il mi, tem fugia</li>
      <li>Conem et ullatus in pratum quas nescil ipsus</li>
    </ul>
  </div>

  <div class="col col-right">
    <p>Voluptis dolupti con es volectus, omnim dipsuntist, diatemp orest, odis iliquae seque dolorrovidem nis dolendest, aborerio maximolut aliqui te nus hitae videllu ptatiatur?</p>
    <p>Rem venim sequaestio inum audaeru ptatam ut apidero excestrum id eum que quatur a perchil luptass.</p>
    <p>Dolenimilit magnam il mi, tem fugia ullatus in pratum quas nescil ipsus ut ut accaboremque magnisq uaeprorem sequia sequam il ipsanim enimus, int ut. Sedi alignatur sam, quas eria quod ma dolor serem fuga.</p>
  </div>

  <div class="spine"><span class="spine-text">Integrated Solutions for</span></div>

  <div class="stats-rule"></div>
  <div class="stats">
    <h2>Luate ma dero odis</h2>
    <div class="stat">
      <svg width="26" height="22" viewBox="0 0 26 22" aria-hidden="true"><polygon points="13,1 25,21 1,21" fill="#dfe8f4"/><polygon points="13,1 25,21 13,21" fill="#8fa9cf"/></svg>
      <span class="stat-value">20%</span>
      <span class="stat-note">Onserepra coruptiis ut facculi esequia dolupta si voluptatis maximpo rendandaessi ut</span>
    </div>
    <div class="stat">
      <svg width="26" height="22" viewBox="0 0 26 22" aria-hidden="true"><polygon points="13,1 25,21 1,21" fill="#dfe8f4"/><polygon points="13,1 25,21 13,21" fill="#8fa9cf"/></svg>
      <span class="stat-value">30%</span>
      <span class="stat-note">Onserepra coruptiis ut facculi esequia dolupta si voluptatis maximpo rendandaessi ut</span>
    </div>
    <div class="stat">
      <svg width="26" height="22" viewBox="0 0 26 22" aria-hidden="true"><polygon points="13,1 25,21 1,21" fill="#dfe8f4"/><polygon points="13,1 25,21 13,21" fill="#8fa9cf"/></svg>
      <span class="stat-value">20%</span>
      <span class="stat-note">Onserepra coruptiis ut facculi esequia dolupta si voluptatis maximpo rendandaessi ut</span>
    </div>
  </div>
</section>

</body>
</html>
```